Simple Clean Distinctive Fleet Graphic

Need design that can be used on truck (new Halvik Strider), and small/large cargo vans (new full size Halvik Porter, small size porter mini). Needs to include company logo, phone (555-314-9072) and “Service, Repair, Remodel” as the main focal point. Needs to also include “(Contractors License) or (CL) 58216,” which is a state requirement but not part of main focal point, just on bottom or off to the side in 2” letters/number.

Target Market(s)

Our core business is resort hotels, HOA's, and high end residential service and remodel projects.

Font styles to use
Sans Serif
Other font styles liked:
• logo is "what time is it" font

```html
<!DOCTYPE html>
<html lang="en">
<head>
<meta charset="utf-8">
<title>Tidewell Fleet Graphic</title>
<link href="https://fonts.googleapis.com/css2?family=Archivo+Black&family=Quicksand:wght@500&family=Saira:wght@300&display=swap" rel="stylesheet">
<style>
  :root {
    --page: #e9e9e9;
    --panel: #ffffff;
    --ink: #231f20;
    --sky: #35a8e0;
    --deep: #0d4fa3;
    --white: #ffffff;
  }
  html, body {
    margin: 0;
    padding: 0;
    width: 957px;
    height: 1200px;
    overflow: hidden;
    background: var(--page);
  }
  .canvas {
    position: relative;
    width: 957px;
    height: 1200px;
  }
  .fleet-panel {
    position: absolute;
    left: 87px;
    top: 765px;
    width: 808px;
    height: 303px;
    background: var(--panel);
    overflow: hidden;
    box-shadow: 2px 3px 4px rgba(0,0,0,0.35);
  }
  .lower-field {
    position: absolute;
    left: 0;
    top: 0;
    width: 808px;
    height: 303px;
  }
  .brand {
    position: absolute;
    left: 110px;
    top: 58px;
    display: flex;
    align-items: center;
    gap: 22px;
  }
  .brand-dot {
    width: 58px;
    height: 58px;
    border-radius: 50%;
    background: var(--sky);
  }
  .brand-name {
    font-family: "Quicksand", sans-serif;
    font-weight: 500;
    font-size: 70px;
    line-height: 1;
    color: var(--ink);
    letter-spacing: -1px;
  }
  .services {
    position: absolute;
    left: 26px;
    top: 194px;
    margin: 0;
    font-family: "Archivo Black", sans-serif;
    font-size: 17px;
    line-height: 1.1;
    letter-spacing: 0.3px;
    color: var(--sky);
  }
  .phone-pill {
    position: absolute;
    left: 38px;
    top: 224px;
    width: 238px;
    height: 29px;
    border-radius: 15px;
    background: linear-gradient(90deg, var(--deep) 0%, #2a86d0 55%, var(--sky) 100%);
    display: flex;
    align-items: center;
    gap: 13px;
    padding-left: 27px;
    box-sizing: border-box;
  }
  .phone-icon {
    width: 16px;
    height: 16px;
    flex: none;
  }
  .phone-number {
    font-family: "Archivo Black", sans-serif;
    font-size: 20px;
    line-height: 1;
    letter-spacing: 0.8px;
    color: var(--white);
  }
  .license {
    position: absolute;
    left: 296px;
    top: 229px;
    font-family: "Saira", sans-serif;
    font-weight: 300;
    font-size: 14px;
    line-height: 1.2;
    letter-spacing: 0.8px;
    color: var(--white);
  }
</style>
</head>
<body>
<main class="canvas">
  <section class="fleet-panel">
    <svg class="lower-field" viewBox="0 0 808 303" role="img" aria-label="Decorative blue and black wave bands across the lower panel">
      <defs>
        <linearGradient id="field-fade" x1="0" x2="0" y1="0" y2="1">
          <stop offset="0" stop-color="#0d4fa3"/>
          <stop offset="0.14" stop-color="#231f20"/>
          <stop offset="1" stop-color="#231f20"/>
        </linearGradient>
      </defs>
      <path fill="url(#field-fade)"
        d="M0 170 C200 160 380 198 520 248 C620 284 720 290 808 262 L808 303 L0 303 Z"/>
    </svg>

    <div class="brand">
      <span class="brand-dot"></span>
      <span class="brand-name">tidewell</span>
    </div>

    <p class="services">SERVICE, REPAIR, REMODEL</p>

    <div class="phone-pill">
      <svg class="phone-icon" viewBox="0 0 24 24" aria-hidden="true">
        <circle cx="12" cy="12" r="12" fill="#ffffff"/>
        <path fill="#0d4fa3" d="M8.2 5.5c.4-.2.9 0 1.1.4l1.1 2.4c.2.4 0 .8-.3 1.1l-1 .8c.6 1.5 1.7 2.7 3.2 3.4l.9-.9c.3-.3.8-.4 1.1-.2l2.3 1.2c.4.2.6.7.4 1.1l-.6 1.6c-.2.5-.7.8-1.2.7C10.6 16.4 7.4 13 6.8 8.4c-.1-.5.2-1 .7-1.2z"/>
      </svg>
      <span class="phone-number">555-314-9072</span>
    </div>

    <span class="license">(CL) 58216</span>
  </section>
</main>
</body>
</html>
```